Harbor Lantern Energy USA - Product Marketing Brochure

Marketing Brochure for new product launch. Please see the attached.
Updates

Hello and thank you all for your patience. Some of you will be receiving our new pictures, please update the design with the new pics. If you do not receive the new pics then please dont worry about updating your design. Thank you so much for your time and energy!

Target Market(s)

Oil & Gas

Font styles to use
Sans Serif

Requirements
Must have
• Must be modern, please try to incorporate our companies colors into the design.

```html
<!DOCTYPE html>
<html lang="en">
<head>
<meta charset="utf-8">
<title>Harbor Lantern Energy USA – Brochure Inside Spread</title>
<link href="https://fonts.googleapis.com/css2?family=Fira+Sans:ital,wght@0,400;0,600;0,700;1,400;1,700&display=swap" rel="stylesheet">
<style>
  :root {
    --brand-red: #b8272d;
    --brand-navy: #3e4a78;
    --ink-navy: #2f3a66;
    --ink-grey: #6b6b6b;
    --paper: #f7f7f7;
    --stage: #e9e9e9;
    --fold: rgba(0,0,0,0.07);
    --photo-truck-a: #c9d2da;
    --photo-truck-b: #e8ebee;
    --map-grey: #cfcfcf;
  }
  * { box-sizing: border-box; margin: 0; padding: 0; }
  html, body {
    width: 1200px; height: 675px; overflow: hidden;
    background: var(--stage);
    font-family: "Fira Sans", Arial, sans-serif;
  }
  .spread {
    position: absolute; left: 90px; top: 57px;
    width: 1020px; height: 560px;
    background: var(--paper);
    box-shadow: 0 12px 30px rgba(0,0,0,0.18);
  }
  .spread-art { position: absolute; inset: 0; }
  .fold { position: absolute; top: 0; bottom: 0; width: 1px; background: var(--fold); }
  .fold--one { left: 340px; }
  .fold--two { left: 680px; }

  .panel { position: absolute; top: 0; width: 340px; height: 560px; }
  .panel--safety { left: 0; padding: 46px 28px 0 30px; }
  .panel--product { left: 340px; padding: 108px 24px 0 26px; }

  .safety-title { font-weight: 600; text-transform: uppercase; line-height: 1.1; }
  .safety-title__lead { display: block; color: var(--brand-red); font-size: 23px; }
  .safety-title__rest { display: block; color: var(--ink-navy); font-size: 19px; margin-top: 2px; }
  .safety-copy {
    margin-top: 18px; color: var(--ink-navy);
    font-size: 12.4px; line-height: 1.36;
  }

  .product-title { color: var(--ink-grey); font-weight: 700; font-size: 21px; line-height: 1.15; }
  .product-lede {
    margin-top: 6px; color: var(--ink-grey);
    font-style: italic; font-weight: 700; font-size: 12.5px; line-height: 1.35;
  }
  .benefits {
    display: flex; align-items: flex-start; gap: 14px; margin-top: 28px;
  }
  .benefit-list { list-style: none; flex: 1; }
  .benefit-list li {
    position: relative; padding-left: 14px;
    color: var(--ink-grey); font-size: 12px; line-height: 1.38; margin-bottom: 4px;
  }
  .benefit-list li::before {
    content: ""; position: absolute; left: 0; top: 6px;
    width: 7px; height: 7px; border-radius: 50%; background: var(--ink-grey);
  }

  .coverage-map {
    position: absolute; left: 712px; top: 250px;
    width: 280px; height: 200px; border-radius: 14px;
    background: var(--map-grey);
  }
</style>
</head>
<body>
  <main class="spread">
    <svg class="spread-art" width="1020" height="560" viewBox="0 0 1020 560">
      <defs>
        <linearGradient id="fleetTone" x1="0" y1="0" x2="0" y2="1">
          <stop offset="0" stop-color="var(--photo-truck-a)"/>
          <stop offset="0.55" stop-color="var(--photo-truck-b)"/>
          <stop offset="1" stop-color="#8a7b6a"/>
        </linearGradient>
        <linearGradient id="driverTone" x1="0" y1="0" x2="1" y2="0">
          <stop offset="0" stop-color="#b9c7d6"/>
          <stop offset="0.4" stop-color="#e6e3cf"/>
          <stop offset="1" stop-color="#eef0f2"/>
        </linearGradient>
      </defs>
      <polygon class="band band--red" points="0,385 190,335 500,560 0,560" fill="var(--brand-red)"/>
      <polygon class="photo photo--fleet" role="img" aria-label="Photo of white fuel tanker trucks parked on a gravel lot"
               points="0,415 190,368 462,560 0,560" fill="url(#fleetTone)"/>
      <polygon class="band band--navy" points="560,0 770,165 1020,85 1020,0" fill="var(--brand-navy)"/>
      <polygon class="photo photo--driver" role="img" aria-label="Photo of a fuel technician in a hard hat standing beside a white tanker truck cab"
               points="600,0 770,130 1020,50 1020,0" fill="url(#driverTone)"/>
    </svg>

    <span class="fold fold--one"></span>
    <span class="fold fold--two"></span>

    <section class="panel panel--safety">
      <h2 class="safety-title">
        <span class="safety-title__lead">Think Safe,</span>
        <span class="safety-title__rest">Work Safe, Home Safe</span>
      </h2>
      <p class="safety-copy">Safety is not just another line item to check off in our business. The more we think it and live it, the better chance we have of getting home to what matters most to all of us. We look at safety from an industry standpoint and we must all work together to ensure our wellbeing and hold one another accountable to best practices and creating a safer working environment for all. We work closely with our associates each day to ensure that we are always taking a proactive approach to safety.</p>
    </section>

    <section class="panel panel--product">
      <h2 class="product-title">Equipment is always at a risk of failing,</h2>
      <p class="product-lede">The Lantern Balancer was designed to keep the process safe and simple and your tanks full.</p>
      <div class="benefits">
        <ul class="benefit-list benefit-list--first">
          <li>Eliminates Red zone fueling,</li>
          <li>No pumps, no motors, reduces mechanical dependency,</li>
          <li>Eliminate fuel lines spread throughout your location,</li>
          <li>Pull Horsepower's forward without disconnecting from the fueling system,</li>
        </ul>
        <ul class="benefit-list benefit-list--second">
          <li>Simple and Safe,</li>
          <li>No more pulling hose between equipment,</li>
          <li>Reduces onsite footprint in comparison to large automation units,</li>
          <li>Reduces fixed costs over traditional automated fueling options,</li>
        </ul>
      </div>
    </section>

    <div class="coverage-map" role="img" aria-label="Map of the United States with the northern plains service states highlighted in red"></div>
  </main>
</body>
</html>
```